Corporate Business Card

Very professional, Modern, Not to busy, include phone address email, website
(253) 555-0174, 61807 19th Street N, Kent, WA 98517, marcus@kestrelbayholding.com, brelvanindustries.com

Target Market(s)

Manufacturing

Industry/Entity Type

Aero, machining, manufacturing, Off road racing

Contact Information for Business Card

Phone, address email, website

```html
<!DOCTYPE html>
<html lang="en">
<head>
<meta charset="utf-8">
<title>Brelvan Industries — Business Card</title>
<link href="https://fonts.googleapis.com/css2?family=Orbitron:wght@500;700;800&display=swap" rel="stylesheet">
<style>
  :root {
    --backdrop: #cddcf1;
    --card: #ffffff;
    --navy: #15346e;
    --red: #d42428;
  }
  * { margin: 0; padding: 0; box-sizing: border-box; }
  html, body {
    width: 1200px;
    height: 1200px;
    overflow: hidden;
    background: var(--backdrop);
    font-family: "Orbitron", sans-serif;
    color: var(--navy);
  }
  .card {
    position: absolute;
    left: 371px;
    width: 459px;
    height: 276px;
    background: var(--card);
  }
  .card--front { top: 247px; }
  .card--back { top: 684px; }

  .brand-name {
    position: absolute;
    font-weight: 800;
    color: var(--navy);
    white-space: nowrap;
    letter-spacing: 0.02em;
  }
  .card--front .brand-name {
    left: 0;
    right: 0;
    top: 118px;
    text-align: center;
    font-size: 27px;
  }
  .front-website {
    position: absolute;
    left: 0;
    right: 0;
    top: 234px;
    text-align: center;
    font-size: 7.5px;
    font-weight: 500;
    letter-spacing: 0.04em;
  }

  .contacts-title {
    position: absolute;
    left: 30px;
    top: 28px;
    font-size: 18px;
    font-weight: 800;
    letter-spacing: 0.04em;
    line-height: 1;
  }
  .contacts-rule {
    position: absolute;
    left: 30px;
    top: 48px;
    width: 140px;
    height: 3px;
    background: var(--red);
  }
  .contact-list {
    position: absolute;
    left: 30px;
    top: 192px;
    list-style: none;
    font-size: 8px;
    font-weight: 500;
    letter-spacing: 0.03em;
    line-height: 14.6px;
  }
  .card--back .brand-name {
    right: 30px;
    top: 218px;
    font-size: 13px;
  }
</style>
</head>
<body>
  <section class="card card--front">
    <div class="brand-name">Brelvan Industries</div>
    <div class="front-website">www.brelvanindustries.com</div>
  </section>

  <section class="card card--back">
    <h2 class="contacts-title">CONTACTS</h2>
    <div class="contacts-rule"></div>
    <ul class="contact-list">
      <li>(253) 555-0174</li>
      <li>marcus@kestrelbayholding.com</li>
      <li>www.brelvanindustries.com</li>
      <li>61807 19th Street N, Kent, WA 98517</li>
    </ul>
    <div class="brand-name">Brelvan Industries</div>
  </section>
</body>
</html>
```